Harborline Safety Courses

I'm currently in the process of setting up a First Aid and Lifeguard Training website. The project has already began through a web designer but he is unable to meet the deadline.
There's is already a landing page
http://www.harborlinesafetycourses.example.au/
In addition he also started to create the website
https://mockups.example.net/view/9c41d7e0-5b2a-4e8f-a613-d02e7bb18c39-2218/?fullscreen
The home page ideally needs to have a different visual and user journey from the quick landing page created
- The Logo in the top left hand corner looks a bit out of whack, maybe it needs to be bigger ??
-The tabs along the top need to be 'designed' and spaced out equally: home, about, courses, contact, gallery. Can we please remove Accredited First Aid and Lifeguard.
-the blue bar with the tag line needs to be redesigned - that was ok for a landing page but not quite right for actual website, it looks clunky
-all the course info needs to be placed under the courses tab not on the home page. I would like a roll down bar ( Check out Tidewater Rescue Aid website on their First Aid Course) so the client can book a date and proceed to the checkout basket. I will supply those soon; this will only apply to the Provide First Aid and Provide Cardiopulmonary Resuscitation Courses.
- The rest of the courses can have an enquire option
-the about paragraphs need to go directly under banner
-then a rolling slider with upcoming courses - with each course, rolling to give the home page some pop
- followed by pictures/ images of recent courses linked to gallery page updates or social feed
-remove newsletter
In addition to this I also have a logo designed via sketch harbor and lots of photos as well as briefs on all the courses that I will offer.
Accredited First Aid and CPR Courses. Lifeguard and Community Safety Programs Programs

```html
<!DOCTYPE html>
<html lang="en">
<head>
<meta charset="utf-8">
<title>Harborline Safety Courses</title>
<link rel="stylesheet" href="https://fonts.googleapis.com/css2?family=Titillium+Web:wght@300;400;600;700&family=Montserrat:wght@400;500;600;700&display=swap">
<style>
:root{
  --navy:#0b1f3a;
  --navy-deep:#06172e;
  --navy-mid:#14365e;
  --blue:#2a9ad6;
  --blue-light:#35a9e0;
  --orange:#f7931e;
  --white:#ffffff;
  --muted:#c9d8e8;
  --teal:#2aa6d8;
  --sand:#c9a97a;
}
*{box-sizing:border-box;margin:0;padding:0}
html,body{width:1200px;height:3524px;overflow:hidden}
body{position:relative;background:var(--navy);font-family:'Montserrat',sans-serif;color:var(--white)}
.abs{position:absolute}
.heading{font-family:'Titillium Web',sans-serif}

/* hero */
.hero{left:0;top:0;width:1200px;height:731px}
.hero-photo{left:0;top:0;width:1200px;height:731px;
  background:
    linear-gradient(180deg,rgba(10,25,50,.55) 0%,rgba(10,25,50,0) 18%),
    radial-gradient(ellipse 150px 260px at 40px 380px,rgba(42,166,216,.9),rgba(42,166,216,0) 100%),
    radial-gradient(ellipse 230px 330px at 1080px 380px,rgba(36,160,214,.95),rgba(36,160,214,0) 100%),
    radial-gradient(ellipse 150px 230px at 530px 320px,rgba(40,150,205,.8),rgba(40,150,205,0) 100%),
    radial-gradient(ellipse 360px 150px at 560px 300px,rgba(240,244,248,.85),rgba(240,244,248,0) 100%),
    radial-gradient(ellipse 170px 120px at 1120px 140px,rgba(28,56,34,.8),rgba(28,56,34,0) 100%),
    radial-gradient(ellipse 120px 40px at 560px 560px,rgba(238,92,38,.55),rgba(238,92,38,0) 100%),
    linear-gradient(180deg,#223f68 0%,#5a86b0 16%,#8fb0cc 24%,#4f7d98 30%,#d2b68a 42%,#c9a778 70%,#b89466 100%)}
.brand{left:110px;top:14px;width:186px;height:160px;display:flex;flex-direction:column;align-items:center;gap:8px}
.brand-mark{width:84px;height:84px;border-radius:50%;border:5px solid var(--blue-light);flex:none}
.brand-name{font-family:'Titillium Web',sans-serif;font-weight:600;font-size:15px;text-align:center;color:var(--orange);line-height:1.15;text-transform:uppercase;letter-spacing:1px}
.nav{left:390px;top:36px}
.nav a{font-family:'Titillium Web',sans-serif;font-size:15px;color:var(--white);text-decoration:none;text-transform:uppercase;position:absolute;white-space:nowrap}
.nav a.active{color:var(--orange)}
.nav a.active::after{content:"";position:absolute;left:0;right:0;bottom:-10px;height:2px;background:var(--orange)}
.tagline-top{left:235px;top:345px;width:723px;height:63px;background:rgba(247,147,30,.94);border-radius:34px 6px 0 0;display:flex;align-items:center;justify-content:center;font-family:'Titillium Web',sans-serif;font-weight:300;font-size:38px;color:var(--white)}
.tagline-bottom{left:235px;top:408px;width:723px;height:70px;background:rgba(53,169,224,.94);border-radius:0 0 0 34px;display:flex;align-items:center;justify-content:center;font-family:'Titillium Web',sans-serif;font-weight:700;font-size:38px;color:var(--white)}

/* about */
.about{left:0;top:731px;width:1200px;height:542px}
.about-title{left:137px;top:818px;font-size:48px;font-weight:700;line-height:1.1}
.about-sub{left:136px;top:875px;font-size:33px;font-weight:300}
.about-rule{left:139px;top:930px;width:62px;height:3px;background:var(--white)}
.about-copy{left:137px;top:957px;width:480px;font-size:14.5px;line-height:1.65}
.about-copy p+p{margin-top:12px}
.btn-outline{border:2px solid var(--white);border-radius:26px;display:flex;align-items:center;justify-content:center;font-weight:600;font-size:13.5px;color:var(--white);text-transform:uppercase}
.about-btn{left:134px;top:1113px;width:168px;height:50px}
.about-photo{left:643px;top:778px;width:442px;height:442px;border-radius:50%;border:16px solid var(--white);
  background:
    linear-gradient(180deg,#8c8577 0%,#b5b2a8 9%,#3f8fd0 14%,rgba(63,143,208,0) 30%),
    radial-gradient(ellipse 110px 70px at 290px 220px,rgba(240,240,240,.8),rgba(240,240,240,0) 100%),
    radial-gradient(ellipse 70px 90px at 160px 200px,rgba(170,170,170,.7),rgba(170,170,170,0) 100%),
    radial-gradient(ellipse 90px 40px at 190px 330px,rgba(246,206,40,.75),rgba(246,206,40,0) 100%),
    radial-gradient(circle at 50% 45%,#4eb0e6,#2a86cc 60%,#1b5f9c)}

/* courses */
.courses-band{left:0;top:1273px;width:1200px;height:1375px;background:linear-gradient(180deg,var(--navy-deep) 0%,var(--navy) 40%,var(--navy-mid) 100%)}
.section-title{width:1200px;left:0;text-align:center;font-family:'Titillium Web',sans-serif;font-weight:700;font-size:38px}
.title-rule{left:572px;width:56px;height:3px;background:var(--blue-light)}
.card{background:var(--navy);border:2px solid var(--blue-light);text-align:center}
.card-photo{width:100%;height:190px}
.card-name{font-weight:700;font-size:14.5px;line-height:1.4;margin-top:16px;text-transform:uppercase}
.card-note{font-size:14.5px;margin-top:4px;color:var(--muted)}
.btn-book{display:inline-flex;align-items:center;justify-content:center;width:135px;height:34px;background:var(--orange);border-radius:18px;font-weight:700;font-size:12px;color:var(--white);margin-top:14px;text-transform:uppercase}
.card.featured{background:var(--white);border:none;box-shadow:0 6px 20px rgba(0,0,0,.35)}
.card.featured .card-photo{height:206px}
.card.featured .card-name{color:var(--navy)}
.card.featured .card-note{color:var(--blue)}
.card.featured .btn-book{width:146px;height:39px;font-size:13px}
.dots{left:576px;top:1883px;display:flex;gap:8px}
.dots span{width:13px;height:13px;border-radius:50%;border:1.5px solid var(--white)}
.dots span.on{background:var(--white)}
.gallery-tile{width:471px;height:230px}
.gallery-btn{left:516px;top:2550px;width:167px;height:50px}

/* contact */
.contact{left:0;top:2648px;width:1200px;height:489px;background:linear-gradient(180deg,#2b93d0 0%,#3aa6de 40%,#6fb6dc 100%)}
.contact-photo{left:0;top:2873px;width:1200px;height:264px;
  background:
    radial-gradient(ellipse 80px 130px at 850px 170px,rgba(56,170,222,.95),rgba(56,170,222,0) 100%),
    radial-gradient(ellipse 60px 120px at 700px 170px,rgba(245,245,245,.95),rgba(245,245,245,0) 100%),
    radial-gradient(ellipse 620px 34px at 600px 70px,rgba(60,44,36,.55),rgba(60,44,36,0) 100%),
    radial-gradient(ellipse 700px 50px at 600px 40px,rgba(30,40,60,.35),rgba(30,40,60,0) 100%),
    linear-gradient(90deg,rgba(220,60,50,0) 0%,rgba(220,60,50,.18) 25%,rgba(220,60,50,0) 40%,rgba(220,60,50,.16) 60%,rgba(220,60,50,0) 70%,rgba(220,60,50,.18) 90%,rgba(220,60,50,0) 100%),
    linear-gradient(180deg,#7fb6d6 0%,#9cc4da 18%,#e9edf1 45%,#f4f5f6 75%,#dfe3e8 100%)}
.contact-title{left:0;top:2718px;width:1200px;text-align:center;font-family:'Titillium Web',sans-serif;font-weight:700;font-size:42px;line-height:1}
.contact-sub{left:0;top:2768px;width:1200px;text-align:center;font-family:'Titillium Web',sans-serif;font-weight:300;font-size:38px;line-height:1}
.contact-btn{left:514px;top:2825px;width:182px;height:45px;background:var(--orange);border-radius:24px;display:flex;align-items:center;justify-content:center;font-weight:700;font-size:16px}

/* footer */
.footer{left:0;top:3137px;width:1200px;height:387px;background:var(--navy-deep)}
.footer-divider{top:3140px;width:1px;height:260px;background:rgba(255,255,255,.08)}
.footer-brand{left:130px;top:3180px;width:190px;height:170px;display:flex;flex-direction:column;align-items:center;gap:10px}
.footer-heading{top:3193px;font-weight:600;font-size:17px;text-transform:uppercase;padding-left:14px;border-left:3px solid var(--orange);line-height:1.1}
.footer-list{top:3243px;font-size:12px;line-height:27px;list-style:none}
.contact-name{left:604px;top:3243px;font-size:12.5px;font-weight:700}
.contact-phone{left:604px;top:3266px;font-size:16px}
.contact-mail{left:604px;top:3297px;font-size:10.5px}
.social{left:890px;display:flex;align-items:center;gap:16px;font-size:12px;line-height:1.45}
.social b{font-weight:700;font-size:13px}
.footer-rule{left:0;top:3454px;width:1200px;height:1px;background:rgba(255,255,255,.1)}
.copyright{left:0;top:3480px;width:1200px;text-align:center;font-size:11px;color:#8aa0b8}
</style>
</head>
<body>

<!-- Hero -->
<section class="abs hero">
  <div class="abs hero-photo" role="img" aria-label="Photo of lifeguard trainees in blue shirts on a beach beside a patrol vehicle with a rescue board on its roof"></div>
  <div class="abs brand">
    <span class="brand-mark"></span>
    <span class="brand-name">Harborline Safety Courses</span>
  </div>
  <nav class="abs nav">
    <a class="active" href="#" style="left:0">Home</a>
    <a href="#" style="left:108px">About</a>
    <a href="#" style="left:218px">Courses</a>
    <a href="#" style="left:345px">Contact</a>
    <a href="#" style="left:473px">Gallery</a>
  </nav>
  <svg class="abs" style="left:996px;top:36px" width="70" height="26" viewBox="0 0 70 26" fill="none" stroke="#fff" stroke-width="2" aria-hidden="true">
    <circle cx="10" cy="10" r="7"/><line x1="15" y1="15" x2="21" y2="21"/>
    <path d="M42 3h4l3 14h15l3-10H48"/><circle cx="51" cy="22" r="2"/><circle cx="62" cy="22" r="2"/>
  </svg>
  <svg class="abs" style="left:66px;top:360px" width="30" height="50" viewBox="0 0 30 50" aria-hidden="true"><polyline points="26,2 4,25 26,48" fill="none" stroke="#fff" stroke-width="4"/></svg>
  <svg class="abs" style="left:1136px;top:360px" width="30" height="50" viewBox="0 0 30 50" aria-hidden="true"><polyline points="4,2 26,25 4,48" fill="none" stroke="#fff" stroke-width="4"/></svg>
  <div class="abs tagline-top">ACCREDITED TRAINING FROM</div>
  <div class="abs tagline-bottom">FIRST AID TO LIFEGUARD PROGRAMS</div>
  <svg class="abs" style="left:587px;top:630px" width="26" height="56" viewBox="0 0 26 56" fill="none" stroke="#fff" stroke-width="2" aria-hidden="true">
    <rect x="2" y="1" width="22" height="34" rx="11"/><line x1="13" y1="8" x2="13" y2="15"/>
    <polyline points="7,41 13,47 19,41"/><polyline points="7,48 13,54 19,48"/>
  </svg>
</section>

<!-- About -->
<section class="abs about">
  <svg class="abs" style="left:0;top:0" width="1200" height="542" viewBox="0 0 1200 542" aria-hidden="true">
    <defs>
      <linearGradient id="aboutGrad" x1="0" y1="0" x2="1" y2="0">
        <stop offset="0" stop-color="#1f7fc2"/>
        <stop offset="1" stop-color="#37a8df"/>
      </linearGradient>
    </defs>
    <rect width="1200" height="542" fill="#0a2240"/>
    <path d="M0 0 H880 A250 250 0 0 1 1130 250 A290 290 0 0 1 840 542 H0 Z" fill="url(#aboutGrad)"/>
  </svg>
</section>
<h2 class="abs heading about-title">ABOUT HARBORLINE</h2>
<p class="abs heading about-sub">SAFETY COURSES</p>
<span class="abs about-rule"></span>
<div class="abs about-copy">
  <p>Lorem ipsum dolor sit amet, consectetur adipiscing elit, sed do eiusmod tempor incididunt ut labore et dolore magna aliqua.</p>
  <p>Ut enim ad minim veniam, quis nostrud exercitation ullamco laboris nisi ut aliquip ex ea commodo consequat. Duis aute irure dolor in reprehenderit in voluptate velit esse cillum dolore</p>
</div>
<a class="abs btn-outline about-btn">Learn More</a>
<div class="abs about-photo" role="img" aria-label="Photo of trainees practising a spinal board rescue in an empty blue pool"></div>

<!-- Upcoming courses -->
<div class="abs courses-band"></div>
<h2 class="abs section-title" style="top:1350px">UPCOMING COURSES</h2>
<span class="abs title-rule" style="top:1402px"></span>

<article class="abs card" style="left:120px;top:1467px;width:297px;height:339px">
  <div class="card-photo" role="img" aria-label="Photo of a rescue practice in a drained blue pool" style="background:radial-gradient(ellipse 70px 50px at 160px 70px,rgba(235,235,235,.75),rgba(235,235,235,0)),radial-gradient(ellipse 60px 22px at 70px 170px,rgba(230,70,50,.7),rgba(230,70,50,0)),linear-gradient(160deg,#3a8fd0,#2d7fc4 50%,#1f5f9e)"></div>
  <h3 class="card-name">Cardiopulmonary<br>Resuscitation</h3>
  <p class="card-note">Limted Places</p>
  <span class="btn-book">Book Now</span>
</article>
<article class="abs card featured" style="left:439px;top:1453px;width:322px;height:368px">
  <div class="card-photo" role="img" aria-label="Photo of lifeguards beside a rescue jet ski" style="background:radial-gradient(ellipse 70px 90px at 60px 140px,rgba(30,90,190,.95),rgba(30,90,190,0)),radial-gradient(ellipse 80px 60px at 260px 110px,rgba(210,40,50,.6),rgba(210,40,50,0)),radial-gradient(ellipse 60px 50px at 300px 170px,rgba(235,235,235,.7),rgba(235,235,235,0)),linear-gradient(180deg,#8fb8da 0%,#5f8a6a 25%,#4b5058 60%,#6d6860 100%)"></div>
  <h3 class="card-name">Provide First Aid<br>HLTAID011</h3>
  <p class="card-note">Limted Places</p>
  <span class="btn-book">Book Now</span>
</article>
<article class="abs card" style="left:776px;top:1467px;width:297px;height:339px">
  <div class="card-photo" role="img" aria-label="Photo of an instructor in a lifeguard shirt holding training equipment" style="background:radial-gradient(ellipse 90px 70px at 170px 160px,rgba(54,170,210,.95),rgba(54,170,210,0)),radial-gradient(ellipse 30px 25px at 95px 130px,rgba(245,220,80,.8),rgba(245,220,80,0)),linear-gradient(160deg,#d48540,#a6622e 50%,#6e3f22)"></div>
  <h3 class="card-name">Cardiopulmonary<br>Resuscitation</h3>
  <p class="card-note">Limted Places</p>
  <span class="btn-book">Book Now</span>
</article>
<div class="abs dots"><span class="on"></span><span></span><span></span></div>

<!-- Gallery -->
<h2 class="abs section-title" style="top:1943px;font-size:30px">RECENT COURSES GALLERY</h2>
<span class="abs title-rule" style="top:1995px"></span>
<div class="abs gallery-tile" style="left:120px;top:2048px;background:radial-gradient(ellipse 70px 110px at 210px 140px,rgba(40,160,210,.9),rgba(40,160,210,0)),radial-gradient(ellipse 60px 100px at 370px 150px,rgba(38,150,205,.85),rgba(38,150,205,0)),radial-gradient(ellipse 60px 100px at 150px 160px,rgba(30,30,36,.8),rgba(30,30,36,0)),linear-gradient(180deg,#5f7d9b 0%,#a9b8c4 30%,#7e93a0 40%,#cdb998 55%,#bfa985 100%)" role="img" aria-label="Photo of instructors and trainees on a beach"></div>
<div class="abs gallery-tile" style="left:600px;top:2048px;background:radial-gradient(ellipse 80px 30px at 290px 190px,rgba(244,206,40,.8),rgba(244,206,40,0)),radial-gradient(ellipse 70px 80px at 150px 110px,rgba(235,235,235,.55),rgba(235,235,235,0)),radial-gradient(ellipse 200px 120px at 380px 70px,rgba(110,190,240,.6),rgba(110,190,240,0)),linear-gradient(160deg,#3aa0e0,#2a86cf 50%,#1e6fb5)" role="img" aria-label="Photo of trainees in a drained pool with a rescue stretcher"></div>
<div class="abs gallery-tile" style="left:120px;top:2290px;height:229px;background:radial-gradient(ellipse 110px 90px at 120px 120px,rgba(250,250,250,.95),rgba(250,250,250,0)),radial-gradient(ellipse 100px 80px at 380px 110px,rgba(240,240,240,.9),rgba(240,240,240,0)),radial-gradient(ellipse 80px 60px at 240px 120px,rgba(60,40,30,.65),rgba(60,40,30,0)),radial-gradient(ellipse 50px 30px at 200px 160px,rgba(240,205,60,.75),rgba(240,205,60,0)),linear-gradient(160deg,#8fd6ea,#d8e6e8 40%,#a88a66 80%,#7a5a3c)" role="img" aria-label="Photo of lifeguard trainees practising resuscitation on a mat"></div>
<div class="abs gallery-tile" style="left:600px;top:2290px;height:229px;background:radial-gradient(ellipse 190px 40px at 200px 130px,rgba(40,170,215,.85),rgba(40,170,215,0)),radial-gradient(ellipse 70px 50px at 400px 130px,rgba(35,35,35,.65),rgba(35,35,35,0)),radial-gradient(ellipse 160px 50px at 330px 60px,rgba(36,72,40,.85),rgba(36,72,40,0)),linear-gradient(180deg,#6f9ccd 0%,#9cbbd9 25%,#4f7f5a 38%,#d9c7a2 55%,#cdb68d 100%)" role="img" aria-label="Photo of a group of lifeguards in blue shirts on the sand"></div>
<a class="abs btn-outline gallery-btn">View Gallery</a>

<!-- Contact -->
<section class="abs contact"></section>
<div class="abs contact-photo" role="img" aria-label="Group photo of lifeguard graduates in white rash shirts on a beach"></div>
<h2 class="abs contact-title">CONTACT US &amp; GET START YOUR</h2>
<p class="abs contact-sub">LIFEGUARD COURSES NOW</p>
<a class="abs contact-btn">CONTACT US</a>

<!-- Footer -->
<footer class="abs footer"></footer>
<span class="abs footer-divider" style="left:369px"></span>
<span class="abs footer-divider" style="left:585px"></span>
<span class="abs footer-divider" style="left:871px"></span>
<div class="abs footer-brand">
  <span class="brand-mark" style="width:96px;height:96px"></span>
  <span class="brand-name">Harborline Safety Courses</span>
</div>

<h4 class="abs footer-heading" style="left:370px">Navigation</h4>
<ul class="abs footer-list" style="left:394px">
  <li>Home</li><li>About Us</li><li>Courses</li><li>Gallery</li><li>Contact Us</li>
</ul>

<h4 class="abs footer-heading" style="left:585px">Contact Us</h4>
<p class="abs contact-name">Dana Whitlock</p>
<p class="abs contact-phone">0400 555 218</p>
<p class="abs contact-mail">dana@harborlinesafetycourses.example.au</p>

<h4 class="abs footer-heading" style="left:871px">Get In Touch</h4>
<div class="abs social" style="top:3250px">
  <span style="width:16px;height:16px;border:2px solid #fff;border-radius:3px"></span>
  <span>Follow us<br><b>Social Page</b></span>
</div>
<div class="abs social" style="top:3310px">
  <span style="width:16px;height:16px;border:2px solid #fff;border-radius:50%"></span>
  <span>Follow us<br><b>Photo Feed</b></span>
</div>

<span class="abs footer-rule"></span>
<p class="abs copyright">© Copyright 2021 Harborline Safety Courses</p>

</body>
</html>
```